" Trata-se de uma construtora em conjunto com um escritório de engenharia e arquitetura para prestar serviços de construção, gerenciamento de obras e projetos e desenho. "

```html
<!DOCTYPE html>
<html lang="pt-BR">
<head>
<meta charset="UTF-8">
<title>Obra Viva Brasil — Quem Somos</title>
<link href="https://fonts.googleapis.com/css2?family=Lato:wght@300;400;700;900&display=swap" rel="stylesheet">
<style>
  :root {
    --header-bg: #3b3e43;
    --accent: #f2c230;
    --ink: #3b3e43;
    --text: #6b6e73;
    --nav-text: #d9dadc;
    --page-bg: #ffffff;
    --hero-dark: #2c2724;
    --hero-mid: #6e6258;
    --hero-light: #d8d2cb;
  }
  * { margin: 0; padding: 0; box-sizing: border-box; }
  html, body {
    width: 1200px; height: 1200px; overflow: hidden;
    background: var(--page-bg);
    font-family: 'Lato', sans-serif;
  }
  .page { width: 1200px; height: 1200px; display: flex; flex-direction: column; }

  .site-header {
    height: 92px; background: var(--header-bg);
    display: flex; align-items: center; justify-content: space-between;
    padding: 0 70px 0 200px;
  }
  .brand { display: flex; align-items: center; gap: 12px; color: var(--accent); }
  .brand-mark { width: 14px; height: 14px; border-radius: 50%; background: var(--accent); }
  .brand-name { font-weight: 700; font-size: 22px; letter-spacing: 3px; }
  .main-nav { display: flex; align-items: center; gap: 28px; }
  .main-nav a {
    color: var(--nav-text); text-decoration: none;
    font-size: 15px; font-weight: 700; letter-spacing: 1.2px;
  }
  .main-nav a.is-active { color: var(--accent); }
  .social-links { display: flex; gap: 10px; margin-left: 20px; }
  .social-dot { width: 12px; height: 12px; border-radius: 50%; background: var(--accent); }

  .hero {
    position: relative; height: 400px;
    display: flex; flex-direction: column; align-items: center; justify-content: center;
  }
  .hero-photo {
    position: absolute; inset: 0;
    background:
      radial-gradient(ellipse at 78% 40%, var(--hero-dark) 0%, transparent 35%),
      radial-gradient(ellipse at 12% 60%, var(--hero-light) 0%, transparent 45%),
      linear-gradient(90deg, var(--hero-light) 0%, var(--hero-mid) 45%, var(--hero-dark) 70%, var(--hero-mid) 100%);
  }
  .hero-photo::after { content: ""; position: absolute; inset: 0; background: rgba(30, 28, 26, 0.35); }
  .hero-kicker {
    position: relative; color: #fff; font-size: 16px; font-weight: 700;
    letter-spacing: 3px; margin-bottom: 6px;
  }
  .hero-title { position: relative; color: #fff; font-weight: 400; font-size: 60px; }
  .hero-title .highlight { color: var(--accent); }

  .about { padding: 48px 200px 0; flex: 1; }
  .section-title {
    text-align: center; color: var(--ink);
    font-size: 22px; font-weight: 700; letter-spacing: 1px;
  }
  .section-rule { width: 300px; height: 2px; background: var(--accent); margin: 12px auto 44px; }
  .about-text { color: var(--text); font-size: 17px; line-height: 1.7; }
  .about-text .highlight { color: var(--accent); }

  .values {
    display: grid; grid-template-columns: 1fr 1fr; column-gap: 70px; row-gap: 40px;
    margin-top: 80px;
  }
  .value { display: flex; align-items: flex-start; gap: 22px; }
  .value-icon { flex: 0 0 48px; }
  .value-text { color: var(--text); font-size: 16px; line-height: 1.6; padding-top: 4px; }
</style>
</head>
<body>
<div class="page">
  <header class="site-header">
    <div class="brand">
      <span class="brand-mark"></span>
      <span class="brand-name">OVB</span>
    </div>
    <nav class="main-nav">
      <a href="#">HOME</a>
      <a href="#" class="is-active">QUEM SOMOS</a>
      <a href="#">SERVIÇOS</a>
      <a href="#">DEPOIMENTOS</a>
      <a href="#">FALE CONOSCO</a>
      <span class="social-links">
        <span class="social-dot"></span><span class="social-dot"></span><span class="social-dot"></span>
      </span>
    </nav>
  </header>

  <section class="hero">
    <div class="hero-photo" role="img" aria-label="Fotografia em close de peças de xadrez de madeira, claras e escuras, desfocadas"></div>
    <p class="hero-kicker">CONHEÇA</p>
    <h1 class="hero-title">um pouquinho <span class="highlight">Sobre Nós</span></h1>
  </section>

  <main class="about">
    <h2 class="section-title">QUEM SOMOS</h2>
    <div class="section-rule"></div>
    <p class="about-text">
      A Obra Viva Brasil nasceu do desejo de uma arquiteta e um engenheiro em provar que a fase de obra não precisa ser um incômodo para o cliente. Com <span class="highlight">uma abordagem transparente, profissional e comprometida</span> iremos fazer com que a obra não seja um obstáculo para a realização de um sonho e sim uma importante parte deste sonho. Para a concretização deste desejo
    </p>

    <div class="values">
      <div class="value">
        <svg class="value-icon" width="48" height="48" viewBox="0 0 48 48"><circle cx="24" cy="24" r="24" fill="var(--accent)"/><path d="M14 25l7 7 14-15" fill="none" stroke="#fff" stroke-width="4" stroke-linecap="round" stroke-linejoin="round"/></svg>
        <p class="value-text">Somos extremamente abertos e honestos com nossos clientes.</p>
      </div>
      <div class="value">
        <svg class="value-icon" width="48" height="48" viewBox="0 0 48 48"><circle cx="24" cy="24" r="24" fill="var(--ink)"/><path d="M14 25l7 7 14-15" fill="none" stroke="#fff" stroke-width="4" stroke-linecap="round" stroke-linejoin="round"/></svg>
        <p class="value-text">Trabalhamos com parceiros de confiança e que compartilham os nossos valores.</p>
      </div>
      <div class="value">
        <svg class="value-icon" width="48" height="48" viewBox="0 0 48 48"><circle cx="24" cy="24" r="24" fill="var(--ink)"/><path d="M14 25l7 7 14-15" fill="none" stroke="#fff" stroke-width="4" stroke-linecap="round" stroke-linejoin="round"/></svg>
        <p class="value-text">Construímos a sua obra como se fosse nossa própria casa.</p>
      </div>
      <div class="value">
        <svg class="value-icon" width="48" height="48" viewBox="0 0 48 48"><circle cx="24" cy="24" r="24" fill="var(--accent)"/><path d="M14 25l7 7 14-15" fill="none" stroke="#fff" stroke-width="4" stroke-linecap="round" stroke-linejoin="round"/></svg>
        <p class="value-text">Cobramos valores justos dos nossos clientes e parceiros.</p>
      </div>
    </div>
  </main>
</div>
</body>
</html>
```